Lunaro! Laundry Detergent Powder Original Scent 500 grams

We need a packaging design for a new product- laundry detergent in powdered form. The first design will be the original scent and we will move on with the other variants once we have successfully launched this first one.

It will be in powdered form, no window on the packaging.

Target Market(s)

Men and Women ages 18-65 years old

Industry/Entity Type

Product

Font styles to use
Serif

Colors
9bcb3c
0255a3
f37122

Requirements
Must have
• Fresh and Clean look; Bright and solid colors (Please see photo attachment for an image guide of the look we are looking for)
• "Lunaro" is Filipino for Fresh, therefore the packaging must convey this.
• Packaging will be flexible bag in 500 gram pouch (3 side seal). Dimensions to follow.
• Product of China
• Net Weight: 500 grams as packed
• Other text to follow once your design is chosen
Nice to have
• Easy to read font on the brand name "Lunaro"
Should not have
• No black background colors

```html
<!DOCTYPE html>
<html lang="en">
<head>
<meta charset="utf-8">
<title>Lunaro! Original Laundry Detergent Powder – 500g Pouch</title>
<link href="https://fonts.googleapis.com/css2?family=Lato:wght@400;700;900&display=swap" rel="stylesheet">
<style>
  :root {
    --page: #ffffff;
    --sky-top: #1cb6ec;
    --sky-bottom: #8bd6f6;
    --teal: #4cc2b4;
    --green: #2fb36a;
    --green-light: #8fd070;
    --green-deep: #5ea83c;
    --brand-blue: #0255a3;
    --accent-orange: #f0542a;
    --navy: #1d3a72;
    --seal: rgba(255,255,255,0.35);
  }
  html, body {
    margin: 0;
    padding: 0;
    width: 888px;
    height: 1200px;
    overflow: hidden;
    background: var(--page);
  }
  .canvas {
    position: relative;
    width: 888px;
    height: 1200px;
  }
  .pouch {
    display: block;
    width: 888px;
    height: 1200px;
  }
  .brand-name {
    font-family: "Lato", sans-serif;
    font-weight: 900;
    fill: var(--brand-blue);
  }
  .variant {
    font-family: "Lato", sans-serif;
    font-weight: 900;
    font-style: italic;
    fill: var(--brand-blue);
  }
  .product-type {
    font-family: "Lato", sans-serif;
    font-weight: 700;
    fill: var(--accent-orange);
    letter-spacing: 1px;
  }
  .net-label, .net-value, .net-note {
    font-family: "Lato", sans-serif;
    fill: var(--navy);
    text-anchor: middle;
  }
  .net-label { font-weight: 400; font-size: 21px; }
  .net-value { font-weight: 700; font-size: 40px; }
  .net-note  { font-weight: 400; font-size: 21px; letter-spacing: 0.5px; }
</style>
</head>
<body>
<div class="canvas">
  <svg class="pouch" viewBox="0 0 888 1200" xmlns="http://www.w3.org/2000/svg">
    <defs>
      <linearGradient id="sky" x1="0" y1="0" x2="0" y2="1">
        <stop offset="0" stop-color="var(--sky-top)"/>
        <stop offset="0.5" stop-color="var(--sky-bottom)"/>
        <stop offset="1" stop-color="var(--sky-top)"/>
      </linearGradient>
      <radialGradient id="bubbleHaze" cx="0.5" cy="0.5" r="0.6">
        <stop offset="0" stop-color="#ffffff" stop-opacity="0.18"/>
        <stop offset="1" stop-color="#ffffff" stop-opacity="0"/>
      </radialGradient>
      <clipPath id="pouchShape">
        <rect x="11" y="79" width="854" height="1039"/>
      </clipPath>
      <path id="typeArc" d="M196,522 A275,275 0 0,0 708,522"/>
    </defs>

    <g clip-path="url(#pouchShape)">
      <!-- background sky -->
      <rect class="sky" x="11" y="79" width="854" height="1039" fill="url(#sky)"/>

      <!-- green waves -->
      <path class="wave wave-teal" d="M11,735 C260,700 620,600 865,470 L865,1118 L11,1118 Z" fill="var(--teal)" opacity="0.85"/>
      <path class="wave wave-green" d="M11,850 C300,820 640,690 865,560 L865,1118 L11,1118 Z" fill="var(--green)"/>
      <path class="wave wave-light" d="M11,960 C320,950 660,820 865,700 L865,1118 L11,1118 Z" fill="var(--green-light)"/>
      <path class="wave wave-deep" d="M11,1090 C340,1080 680,960 865,880 L865,1118 L11,1118 Z" fill="var(--green-deep)"/>

      <!-- seal stripes -->
      <g class="seal seal-top" stroke="var(--seal)" stroke-width="2">
        <line x1="11" y1="92" x2="865" y2="92"/>
        <line x1="11" y1="100" x2="865" y2="100"/>
        <line x1="11" y1="108" x2="865" y2="108"/>
      </g>
      <g class="seal seal-bottom" stroke="var(--seal)" stroke-width="2">
        <line x1="11" y1="1090" x2="865" y2="1090"/>
        <line x1="11" y1="1098" x2="865" y2="1098"/>
        <line x1="11" y1="1106" x2="865" y2="1106"/>
      </g>

      <!-- soap bubble area -->
      <rect class="bubbles" x="90" y="140" width="740" height="940" fill="url(#bubbleHaze)" role="img" aria-label="Scattered transparent soap bubbles floating across the pouch"/>
    </g>

    <!-- brand block -->
    <circle class="brand-disc" cx="452" cy="404" r="172" fill="#ffffff"/>
    <text class="brand-name" x="211" y="484" font-size="124" textLength="510" lengthAdjust="spacingAndGlyphs">Lunaro!</text>
    <text class="variant" x="456" y="539" font-size="36" textLength="202" lengthAdjust="spacingAndGlyphs">ORIGINAL</text>

    <text class="product-type" font-size="36">
      <textPath href="#typeArc" startOffset="50%" text-anchor="middle">LAUNDRY DETERGENT POWDER</textPath>
    </text>

    <!-- net weight -->
    <text class="net-label" x="702" y="995">Net Weight</text>
    <text class="net-value" x="702" y="1040">500g</text>
    <text class="net-note" x="702" y="1070">as packed</text>
  </svg>
</div>
</body>
</html>
```